Timber panel for yoga trail in the forest

We are planning a yoga trail in the forest. The trail will have different workout areas. On each work out area we will place a wooden panel with a picture of the yoga excercise and a second wooden panel with a short description of the excercise. We need 5 new drawings of five different yoga excercises. The drawings shoulderstand be in line with the existing drawings of the yoga excercises (same stile, one same, same shape ...). In addition to the 5 drawings we need 14 text panels with the description of the excercise. The panels have the size of a A4. The font shoulderstand fit to the existing font on the existing drawings of the yoga excercise. the title Should be highlighted in comparison to the body text. Attached you find the existing Pictures and the new Pictures Which we need. More Over you find the text.

Target Market(s)

switzerland

Industry/Entity Type

Tourism

Font styles to use
Sans Serif

Requirements
Must have
• 5 excercixe drawings and 14 text panels same stile as the existing drawings.

```html
<!DOCTYPE html>
<html lang="de">
<head>
<meta charset="utf-8">
<title>Umkehrhaltung – Yogaweg Tafel</title>
<link href="https://fonts.googleapis.com/css2?family=Arimo:wght@700&display=swap" rel="stylesheet">
<style>
  :root {
    --panel-bg: #ffffff;
    --ink: #000000;
  }
  html, body {
    margin: 0;
    padding: 0;
    width: 1200px;
    height: 848px;
    overflow: hidden;
    background: var(--panel-bg);
  }
  .panel {
    position: relative;
    width: 1200px;
    height: 848px;
    background: var(--panel-bg);
    color: var(--ink);
    font-family: "Arimo", Arial, Helvetica, sans-serif;
    font-weight: 700;
  }
  .exercise-title {
    position: absolute;
    top: 175px;
    left: 0;
    width: 1200px;
    margin: 0;
    text-align: center;
    font-size: 76px;
    line-height: 92px;
    font-weight: 700;
  }
  .exercise-description {
    position: absolute;
    top: 425px;
    left: 116px;
    width: 1000px;
    margin: 0;
    font-size: 45px;
    line-height: 60px;
  }
</style>
</head>
<body>
  <main class="panel">
    <h1 class="exercise-title">Umkehrhaltung<br>(Viparita Karani)</h1>
    <p class="exercise-description">Auf den Rücken legen. Holz unter das<br>Gesäss legen. Beine nach oben,<br>Richtung Himmel, strecken. Atme tief<br>und gleichmässig ein und aus.</p>
  </main>
</body>
</html>
```